Infographic - post exit survey

An infographic is required for the top of some marketing collateral on the topic of 'post exit survey'. This survey is conducted for ex-employees who have left the organisation after a period of at least 1 month. The infographic needs to be clear, simple and easy to understand without too many words. Graphics need to be kept simple whilst utilising the LUMV brand colours.
Target Market(s)
Commercial, non for profit, aged care and disability sectors
Industry/Entity Type
Marketing
Font styles to use
Sans Serif
Colors
0355a3
3176b5
85acd3
cedeed
e34197
Requirements
Must have
- We are a HR consulting firm so this must be professional and to the point. We want it to be clear, concise and to the point. Not too heavy on the text. Please use LUMV Consulting colors. You can find our color scheme on our website: lumvadvise.com.au

```html
<!DOCTYPE html>
<html lang="en">
<head>
<meta charset="utf-8">
<title>Post Exit Survey</title>
<link rel="stylesheet" href="https://fonts.googleapis.com/css2?family=Russo+One&family=Exo+2:wght@400;600&display=swap">
<style>
  :root {
    --brand-navy: #0355a3;
    --brand-blue: #3176b5;
    --brand-sky: #85acd3;
    --brand-mist: #cedeed;
    --brand-pink: #e34197;
    --white: #ffffff;
  }
  * { box-sizing: border-box; margin: 0; padding: 0; }
  html, body { width: 1200px; height: 2250px; overflow: hidden; }
  body { position: relative; font-family: "Exo 2", Arial, sans-serif; background: var(--brand-mist); }
  .backdrop { position: absolute; left: 0; top: 0; }
  .abs { position: absolute; }

  .top-strip { left: 0; top: 0; width: 1200px; height: 95px; background: var(--brand-navy); }
  .title-band { left: 0; top: 95px; width: 1200px; height: 172px; background: var(--brand-mist);
    display: flex; align-items: center; justify-content: center; }
  .title { font-family: "Russo One", Arial, sans-serif; font-size: 82px; color: var(--brand-navy); font-weight: 400; }

  .subtitle { left: 0; top: 305px; width: 1200px; text-align: center; color: var(--white);
    font-size: 40px; line-height: 1.05; letter-spacing: 0.6px; }

  .exit-word { left: 660px; top: 477px; width: 540px; height: 90px;
    background: linear-gradient(90deg, rgba(133,172,211,0) 0%, rgba(206,222,237,0.9) 18%, #ffffff 45%, #dfe9f4 75%, rgba(133,172,211,0.4) 100%); }

  .section-tag { left: 0; width: 608px; height: 74px; background: var(--brand-sky); color: var(--white);
    font-size: 34px; letter-spacing: 0.5px; display: flex; align-items: center; justify-content: center; }
  .tag-believe { top: 561px; }
  .tag-different { top: 922px; }
  .section-copy { left: 65px; width: 480px; text-align: center; color: var(--white);
    font-size: 27px; line-height: 1.04; letter-spacing: 0.6px; }
  .copy-believe { top: 666px; }
  .copy-different { top: 1018px; }

  .keyhole-scene { left: 752px; top: 552px; width: 342px; height: 748px;
    background: linear-gradient(180deg, #ffffff 0%, #eaf1f8 55%, #d4e2f0 100%); }

  .how-band { left: 0; top: 1372px; width: 1200px; height: 83px; background: var(--brand-sky); color: var(--white);
    font-size: 34px; letter-spacing: 0.5px; display: flex; align-items: center; justify-content: center; }

  .step-text { color: var(--brand-navy); font-size: 26px; line-height: 1.02; letter-spacing: 0.5px; text-align: center; }
  .step-email { left: 440px; top: 1562px; width: 270px; }
  .step-questions { left: 220px; top: 1745px; width: 420px; }
  .step-minimum { left: 60px; top: 1926px; width: 470px; }
  .step-graph { left: 140px; top: 2096px; width: 460px; }

  .icon { position: absolute; }
  .handshake { left: 935px; top: 1926px; width: 125px; height: 50px; background: var(--white); border-radius: 4px; }
</style>
</head>
<body>

<svg class="backdrop" width="1200" height="2250" viewBox="0 0 1200 2250" aria-hidden="true">
  <defs>
    <linearGradient id="heroFade" x1="0" y1="0" x2="0" y2="1">
      <stop offset="0" stop-color="#0355a3"/>
      <stop offset="0.45" stop-color="#2266ab"/>
      <stop offset="1" stop-color="#4585c3"/>
    </linearGradient>
    <linearGradient id="wedgeFade" x1="0" y1="0" x2="1" y2="0">
      <stop offset="0" stop-color="#4886c2"/>
      <stop offset="1" stop-color="#a9c5e2"/>
    </linearGradient>
  </defs>
  <rect x="0" y="267" width="1200" height="1105" fill="url(#heroFade)"/>
  <polygon points="1200,1317 1200,1372 840,1372" fill="#cedeed"/>
  <rect x="0" y="1455" width="1200" height="795" fill="#cedeed"/>
  <polygon points="0,1455 700,1455 0,1622" fill="url(#wedgeFade)"/>
  <polygon points="0,1585 520,1490 0,1600" fill="#a4c1df" opacity="0.8"/>
  <polygon points="810,1503 1200,1503 1200,1683 810,1683 735,1593" fill="#0355a3"/>
  <polygon points="675,1683 1200,1683 1200,1866 675,1866 615,1775" fill="#3176b5"/>
  <polygon points="570,1866 1200,1866 1200,2049 570,2049 518,1957" fill="#85acd3"/>
  <polygon points="675,2049 1200,2049 1200,2250 675,2250 615,2150" fill="#ffffff"/>
</svg>

<div class="abs top-strip"></div>
<header class="abs title-band"><h1 class="title">Post Exit Survey</h1></header>

<p class="abs subtitle">Only for ex-employees<br>who have left after a period of at least 1 month</p>

<div class="abs exit-word" role="img" aria-label="Motion-blurred EXIT lettering"></div>

<div class="abs section-tag tag-believe">WE BELIEVE</div>
<p class="abs section-copy copy-believe">People are more likely to be more honest once they have been away from the organisation for a period of time, and are more likely to respond when it is delivered by an impartial third party</p>

<div class="abs section-tag tag-different">WE ARE DIFFERENT</div>
<p class="abs section-copy copy-different">You can compared responses from a standard Exit Survey versus a Post Exit Survey for the same organisation.<br>And the responses were markedly different</p>

<div class="abs keyhole-scene" role="img" aria-label="Illustration of a businessman silhouette walking out through a large white keyhole"></div>

<div class="abs how-band">HOW WE WORK ?</div>

<p class="abs step-text step-email">Receive an email<br>after 1 mounth</p>
<svg class="icon" style="left:926px;top:1522px" width="130" height="160" viewBox="0 0 130 160" aria-hidden="true">
  <rect x="2" y="4" width="118" height="138" rx="8" fill="#ffffff"/>
  <rect x="12" y="2" width="8" height="10" fill="#3176b5"/>
  <rect x="30" y="2" width="8" height="10" fill="#3176b5"/>
  <rect x="12" y="14" width="66" height="10" fill="#3176b5"/>
  <text x="14" y="22" font-family="Exo 2, Arial, sans-serif" font-size="8" font-weight="600" fill="#e34197">1 MOUNTH</text>
  <g fill="#85acd3">
    <rect x="12" y="30" width="50" height="4"/><rect x="12" y="38" width="50" height="4"/>
    <rect x="12" y="46" width="50" height="4"/><rect x="12" y="54" width="50" height="4"/>
  </g>
  <rect x="66" y="30" width="4" height="28" fill="#0355a3"/>
  <line x1="62" y1="90" x2="88" y2="112" stroke="#3176b5" stroke-width="3"/>
  <circle cx="99" cy="123" r="33" fill="#3176b5"/>
  <rect x="86" y="112" width="26" height="18" fill="#ffffff"/>
  <polyline points="86,112 99,122 112,112" fill="none" stroke="#3176b5" stroke-width="2"/>
</svg>

<p class="abs step-text step-questions">consists of 10 question<br>questionnaire</p>
<svg class="icon" style="left:822px;top:1702px" width="230" height="148" viewBox="0 0 230 148" aria-hidden="true">
  <rect x="0" y="0" width="135" height="146" rx="6" fill="#ffffff"/>
  <g stroke="#e34197" stroke-width="3" fill="none">
    <polyline points="14,22 20,28 30,16"/>
    <polyline points="14,50 20,56 30,44"/>
    <path d="M16,72 L28,84 M28,72 L16,84"/>
    <polyline points="14,106 20,112 30,100"/>
    <polyline points="14,132 20,138 30,126"/>
  </g>
  <g fill="#3176b5">
    <rect x="42" y="18" width="78" height="10"/><rect x="42" y="46" width="78" height="10"/>
    <rect x="42" y="74" width="78" height="10"/><rect x="42" y="102" width="78" height="10"/>
    <rect x="42" y="128" width="78" height="10"/>
  </g>
  <polygon points="214,40 224,46 190,118 180,112" fill="#85acd3"/>
  <polygon points="180,112 190,118 200,124 176,130" fill="#9dbde0"/>
</svg>

<p class="abs step-text step-minimum">minimum of 3 exit surveys<br>provided to the organisation</p>
<svg class="icon" style="left:700px;top:1905px" width="230" height="90" viewBox="0 0 230 90" aria-hidden="true">
  <g transform="rotate(-12 40 45)">
    <rect x="2" y="12" width="46" height="62" fill="#ffffff"/>
    <rect x="34" y="10" width="46" height="62" fill="#ffffff" stroke="#85acd3"/>
    <rect x="66" y="8" width="46" height="62" fill="#ffffff" stroke="#85acd3"/>
    <g stroke="#e34197" stroke-width="2"><path d="M72,20h6M72,32h6M72,44h6M72,56h6"/></g>
    <g stroke="#3176b5" stroke-width="3"><path d="M82,20h24M82,32h24M82,44h24M82,56h24"/></g>
  </g>
  <polygon points="198,40 208,40 208,34 220,46 208,58 208,52 198,52" fill="#3176b5"/>
</svg>
<div class="abs handshake" role="img" aria-label="Handshake icon"></div>

<p class="abs step-text step-graph">Responses a graphed against<br>the 10 main reasons why<br>people leave their jobs</p>
<svg class="icon" style="left:810px;top:2074px" width="240" height="130" viewBox="0 0 240 130" aria-hidden="true">
  <g stroke="#3176b5" stroke-width="1.5">
    <line x1="14" y1="4" x2="236" y2="4"/><line x1="14" y1="34" x2="236" y2="34"/>
    <line x1="14" y1="64" x2="236" y2="64"/><line x1="14" y1="94" x2="236" y2="94"/>
    <line x1="14" y1="124" x2="236" y2="124"/><line x1="14" y1="4" x2="14" y2="124"/>
  </g>
  <g fill="#3176b5">
    <rect x="0" y="0" width="8" height="8"/><rect x="0" y="30" width="8" height="8"/>
    <rect x="0" y="60" width="8" height="8"/><rect x="0" y="90" width="8" height="8"/>
    <rect x="0" y="120" width="8" height="8"/>
  </g>
  <g fill="#e34197">
    <rect x="24" y="28" width="34" height="96"/>
    <rect x="66" y="64" width="34" height="60"/>
    <rect x="114" y="96" width="36" height="28"/>
    <rect x="162" y="104" width="36" height="20"/>
  </g>
</svg>

</body>
</html>
```